Create professional business cards using the attached logo previously designed using PixelForge. Would like to see a business card that stands out from the crowd.

One side should just have our logo and our business name ie Roadlamp Consulting Partners, and the other side should have a smaller version of logo and company name, but together with our business details detailed below. Two cards will need to be produced for myself and my business partner

Target Market(s)

Professional financial advice to streetlighting engineers and finance people.

Industry/Entity Type

Business

Contact Information for Business Card

The business card will need to contain; name, title (ie Director, email, mobile number, and website address.

Font styles to use
Other font styles liked:
• HoratioB and HoratioM

Requirements
Must have
• We would like modern clean looking professional business cards that incorprates the attached .ai file logo. Font used is HoratioB and HoratioM and the name of the company is Roadlamp Consulting Partners.
• One side should just have our logo and our business name ie Roadlamp Consulting Partners, and the other side should have a smaller version of logo and company name, but together with our business details as above.
Nice to have
• We would potentially like to emboss the logo and name Roadlamp Consulting Partners Ltd. Perhaps something that reflects the transition from night to day eg white on one side, black on the other.
Should not have
• We are open minded. Do not want anything that would appear as a stock copy and paste from a 'normal' business card website eg CardMilo

```html
<!DOCTYPE html>
<html lang="en">
<head>
<meta charset="utf-8">
<title>Roadlamp Consulting Partners – Business Cards</title>
<link rel="stylesheet" href="https://fonts.googleapis.com/css2?family=Jost:wght@400;500;600&display=swap">
<style>
  :root {
    --backdrop: #8e908f;
    --card-light: #e4e5e9;
    --card-dark: #2a2a2a;
    --ink: #141414;
    --ink-light: #f2f2f2;
    --accent: #c2388f;
  }
  * { box-sizing: border-box; margin: 0; padding: 0; }
  html, body {
    width: 1200px;
    height: 900px;
    overflow: hidden;
    background: var(--backdrop);
    font-family: "Jost", "Futura", sans-serif;
    color: var(--ink);
  }
  .stage { position: relative; width: 1200px; height: 900px; }

  .card {
    position: absolute;
    width: 290px;
    height: 522px;
    overflow: hidden;
  }
  .card--front { left: 229px; top: 115px; background: var(--card-light); }
  .card--back  { left: 622px; top: 237px; background: var(--card-dark); }

  /* Brand mark (name set as text) */
  .brand {
    display: flex;
    align-items: center;
    gap: 7px;
    font-weight: 500;
    letter-spacing: 0.02em;
    text-transform: uppercase;
  }
  .brand__dot { flex: none; border-radius: 50%; background: var(--accent); }

  .card--front .brand {
    position: absolute;
    left: 33px;
    top: 52px;
    font-size: 11px;
    line-height: 1.25;
    color: var(--ink);
  }
  .card--front .brand__dot { width: 16px; height: 16px; }

  .card--back .brand {
    position: absolute;
    left: 0;
    right: 0;
    top: 200px;
    flex-direction: column;
    gap: 16px;
    text-align: center;
    color: var(--ink-light);
    font-size: 17px;
    line-height: 1.3;
  }
  .card--back .brand__dot { width: 56px; height: 56px; }

  /* Person */
  .person { position: absolute; left: 33px; top: 230px; }
  .person__name { font-size: 25px; font-weight: 600; line-height: 1.1; }
  .person__title {
    margin-top: 6px;
    font-size: 13px;
    font-weight: 500;
    letter-spacing: 0.02em;
    text-transform: uppercase;
  }

  .contact {
    position: absolute;
    left: 33px;
    top: 315px;
    list-style: none;
    font-size: 13px;
    line-height: 18.5px;
  }

  .company {
    position: absolute;
    left: 33px;
    bottom: 36px;
    font-size: 19px;
    font-weight: 500;
    line-height: 25px;
    text-transform: uppercase;
    white-space: nowrap;
  }
</style>
</head>
<body>
<main class="stage">

  <section class="card card--front" aria-label="Business card, details side">
    <div class="brand">
      <span class="brand__dot"></span>
      <span>Roadlamp<br>Consulting Partners</span>
    </div>

    <div class="person">
      <h1 class="person__name">Mark Ellison</h1>
      <p class="person__title">Director</p>
    </div>

    <ul class="contact">
      <li>+1 800 555 0147</li>
      <li>mark@roadlampcp.com</li>
      <li>www.roadlampcp.com</li>
    </ul>

    <p class="company">Roadlamp<br>Consulting Partners</p>
  </section>

  <section class="card card--back" aria-label="Business card, brand side">
    <div class="brand">
      <span class="brand__dot"></span>
      <span>Roadlamp<br>Consulting Partners</span>
    </div>
  </section>

</main>
</body>
</html>
```